Website Landing Page for Brightfall Systems

Create a custom designed website landing page for our business. Looking for a professional upscale design that incorporates our logo and logo colors into the theme. I want a standard fixed frame website, not a constant scrolling format that seems to be the trend. To start with I'm looking for more of the graphic design part, maybe a concept or theme, I don't expect to see a finished project. Not interested in generic templates or layouts.

The name of our company is Brightfall Systems and I've attached our logo below. I'd like to have the web page have the same look and feel of our logo, as well as the colors. Our company, Brightfall Systems does system design, installation, and programming, of residential and commercial Audio/Video and Automation systems. We do home theaters, lighting and building automation, video conferencing systems, security camera installations, conference rooms, projectors, distributed audio systems, and similar Technology projects. This will be a professional services/informational website. We will not sell products on this website. This website will be used to advertise our company and communicate our services to prospective customers. Having a well designed, professional and clean website is one way we want to distinguish our company from the competition.

Here are some examples of what I consider a professional well designed website
http://www.qorlamstudio.com/Work/

Last year we had our tradlo store designed (with PixelMarket) and I'm really happy with the way it turned out. You can see it at www.HolvenGearDepot.com I consider this to be a great design and looking for the same level of quality with this new website. However, do not copy or use any part of this design in this new project. This tradlo store is completely separate from our other company Brightfall Systems. I only mention this tradlo store an an example of good work.

Reason: Still going through designs.

Reason: Still working on project and have not had time to review all designs and request revisions.

Reason: Sill going through designs and requesting revisions

Reason: still going through all the submissions we received.

Target Market(s)

People interested in Audio/Video, home theaters, home automation. We do sales, system design, and programming. We typically work on larger projects with both residential and commercial customers.

Industry/Entity Type

Business

Number of Pages Required

1 page

Requirements
Must have
• Great design elements. Please use a white background. I think white goes well with our logo colors.

```html
<!DOCTYPE html>
<html lang="en">
<head>
<meta charset="utf-8">
<title>Brightfall Systems</title>
<link href="https://fonts.googleapis.com/css2?family=Dosis:wght@400;500;600;700;800&display=swap" rel="stylesheet">
<style>
:root{
  --green:#7ed957;
  --blue:#3e8fdf;
  --sky:#5b9ee6;
  --yellow:#f4ec1c;
  --ink:#33333d;
  --text:#444;
  --disc:#ededed;
  --white:#fff;
  --dark:#1d1b1a;
}
*{margin:0;padding:0;box-sizing:border-box}
html,body{width:1200px;height:1200px;overflow:hidden;background:var(--white)}
body{font-family:'Dosis',sans-serif;color:var(--text);position:relative}
.top-rule{position:absolute;top:0;left:0;width:1200px;height:3px;background:var(--green)}
.site-header{position:absolute;top:3px;left:0;width:1200px;height:69px}
.brand{position:absolute;left:216px;top:11px;display:flex;align-items:center;gap:10px}
.brand-mark{width:46px;height:46px;border-radius:50%;background:var(--blue)}
.brand-name{font-weight:600;font-size:17px;line-height:16px;color:var(--blue);letter-spacing:.5px;width:110px}
.btn-contact{position:absolute;left:882px;top:21px;width:102px;height:27px;border-radius:14px;background:var(--green);color:var(--white);font-weight:600;font-size:13px;display:flex;align-items:center;justify-content:center}
.hero{position:absolute;top:72px;left:0;width:1200px;height:480px;background:linear-gradient(180deg,#5c9fe8 0%,#5a9be4 60%,#6aa6e8 100%);text-align:center;color:var(--white)}
.hero h1{position:absolute;top:164px;left:0;width:1200px;font-weight:800;font-size:40px;letter-spacing:.5px}
.hero h2{position:absolute;top:212px;left:0;width:1200px;font-weight:600;font-size:21px}
.hero h2 em{font-style:normal;color:var(--yellow)}
.hero p{position:absolute;top:246px;left:306px;width:588px;font-size:9.6px;line-height:16px}
.arrow{position:absolute;top:216px}
.arrow-prev{left:214px}.arrow-next{left:958px}
.dots{position:absolute;top:496px;left:0;width:1200px;display:flex;justify-content:center;gap:8px;top:424px}
.dots span{width:8px;height:8px;border-radius:50%;background:var(--yellow)}
.dots span:first-child{background:var(--white)}
.needs h3{position:absolute;left:216px;top:594px;font-weight:600;font-size:20px;color:var(--ink)}
.needs p.intro{position:absolute;left:216px;top:635px;width:560px;font-size:9.4px;line-height:16px}
.service{position:absolute;width:260px}
.service .disc{position:absolute;left:0;top:0;width:80px;height:80px;border-radius:50%;background:var(--disc);display:flex;align-items:center;justify-content:center}
.service h4{position:absolute;left:103px;top:6px;font-weight:600;font-size:13px;color:var(--ink);white-space:nowrap}
.service p{position:absolute;left:103px;top:30px;width:140px;font-size:8.8px;line-height:13px}
.btn-more{position:absolute;left:744px;top:854px;width:101px;height:26px;border:2px solid var(--green);border-radius:13px;color:var(--green);font-weight:600;font-size:13px;display:flex;align-items:center;justify-content:center}
.solutions{position:absolute;top:982px;left:0;width:1200px;height:218px;background:linear-gradient(180deg,#2a2624 0%,#1c1a19 100%);text-align:center;color:var(--white)}
.solutions h2{position:absolute;top:132px;left:0;width:1200px;font-weight:500;font-size:32px;line-height:50px}
</style>
</head>
<body>
<div class="top-rule"></div>
<header class="site-header">
  <div class="brand"><span class="brand-mark"></span><span class="brand-name">BRIGHTFALL SYSTEMS</span></div>
  <a class="btn-contact">Contact</a>
</header>

<section class="hero" role="img" aria-label="City skyline photograph tinted blue">
  <h1>TAKING THINGS TO THE NEXT LEVEL</h1>
  <h2>LET US PROVIDE YOU WITH THE BEST <em>AUDIO/VIDEO</em> SERVICE OUT THERE</h2>
  <p>Sed euismod arcu id justo feugiat venenatis eu at ex. Class aptent taciti sociosqu ad litora torquent per conubia nostra, per inceptos himenaeos. Maecenas tristique pellentesque arcu, non molestie risus accumsan quis. Praesent molestie massa a libero tempus rutrum. Phasellus maximus maximus sem, sagittis vulputate ligula. Sed nulla quam, porta vel diam id, interdum vehicula tortor. Cras tristique dolor ante, eu blandit magna luctus vitae. Curabitur lorem risus, blandit ornare luctus quis, facilisis ut arcu. Suspendisse gravida ac elit sit amet aliquet.</p>
  <svg class="arrow arrow-prev" width="28" height="48" viewBox="0 0 28 48"><polyline points="25,2 3,24 25,46" fill="none" stroke="#fff" stroke-width="2"/></svg>
  <svg class="arrow arrow-next" width="28" height="48" viewBox="0 0 28 48"><polyline points="3,2 25,24 3,46" fill="none" stroke="#fff" stroke-width="2"/></svg>
  <div class="dots"><span></span><span></span><span></span></div>
</section>

<section class="needs">
  <h3>We Can Meet All Your Needs</h3>
  <p class="intro">In ante sem, efficitur nec sagittis sit amet, lobortis non tortor. Etiam diam orci, vulputate nec lacinia a, imperdiet vel eros. Nulla sodales sollicitudin blandit. Sed in consectetur enim. Proin sed mauris tincidunt, condimentum metus vitae, vulputate lectus. Sed nec accumsan orci. Vivamus vel placerat metus, vel volutpat mi. Fusce ultrices malesuada dui pretium semper.</p>

  <div class="service" style="left:216px;top:726px">
    <div class="disc"><svg width="56" height="50" viewBox="0 0 56 50" fill="#33333d"><rect x="16" y="2" width="10" height="42" rx="1"/><rect x="30" y="2" width="10" height="42" rx="1"/><circle cx="21" cy="10" r="3" fill="#ededed"/><circle cx="21" cy="20" r="3" fill="#ededed"/><circle cx="21" cy="30" r="3" fill="#ededed"/><circle cx="35" cy="10" r="3" fill="#ededed"/><circle cx="35" cy="20" r="3" fill="#ededed"/><circle cx="35" cy="30" r="3" fill="#ededed"/><path d="M10 14q-6 9 0 18M5 10q-9 13 0 26M46 14q6 9 0 18M51 10q9 13 0 26" fill="none" stroke="#33333d" stroke-width="2.5"/><rect x="16" y="44" width="4" height="4"/><rect x="36" y="44" width="4" height="4"/></svg></div>
    <h4>Home Theatre</h4>
    <p>Pellentesque venenatis nibh et est semper, laoreet ultrices nisi condimentum.</p>
  </div>
  <div class="service" style="left:480px;top:726px">
    <div class="disc"><svg width="56" height="52" viewBox="0 0 56 52" fill="#33333d"><circle cx="10" cy="10" r="6"/><circle cx="46" cy="10" r="6"/><circle cx="28" cy="6" r="6"/><path d="M20 16h16v18H20z"/><path d="M2 20h14v14h6v16h-6V40H6v10H2z"/><path d="M54 20H40v14h-6v16h6V40h10v10h4z"/></svg></div>
    <h4>Conference Rooms</h4>
    <p>Vestibulum viverra in elit sed semper. Nam a erat sit amet massa elementum vulputate.</p>
  </div>
  <div class="service" style="left:744px;top:726px">
    <div class="disc"><svg width="56" height="52" viewBox="0 0 56 52" fill="#33333d"><path d="M12 6l36 18-6 10-36-18z"/><rect x="8" y="2" width="8" height="6" transform="rotate(28 12 5)"/><path d="M22 26v14H4v8h26V30z"/></svg></div>
    <h4>Security Camera Install</h4>
    <p>Nam scelerisque lorem a semper blandit.</p>
  </div>
  <div class="service" style="left:216px;top:854px">
    <div class="disc"><svg width="62" height="36" viewBox="0 0 62 36" fill="#33333d"><rect x="2" y="8" width="58" height="20" rx="2"/><circle cx="31" cy="15" r="9" fill="#ededed"/><circle cx="31" cy="15" r="6"/><rect x="6" y="28" width="8" height="5"/><rect x="48" y="28" width="8" height="5"/><rect x="0" y="14" width="12" height="2" fill="#ededed"/><rect x="50" y="14" width="12" height="2" fill="#ededed"/></svg></div>
    <h4>Projectors</h4>
    <p>Aliquam eu lacus sollicitudin, aliquam nunc vitae, malesuada purus.</p>
  </div>
  <div class="service" style="left:480px;top:854px">
    <div class="disc"><svg width="44" height="56" viewBox="0 0 44 56" fill="#33333d"><path d="M22 2a20 20 0 0 1 12 36v8H10v-8A20 20 0 0 1 22 2z"/><rect x="13" y="48" width="18" height="4"/><rect x="16" y="52" width="12" height="4" rx="2"/><path d="M18 40V24h8v16M16 24a3 3 0 1 1 4-3M28 24a3 3 0 1 0-4-3" fill="none" stroke="#ededed" stroke-width="2.5"/></svg></div>
    <h4>Lighting/Automation</h4>
    <p>Aenean et viverra augue. Morbi euismod consequat tellus, nec ultricies diam fermentum quis.</p>
  </div>
  <a class="btn-more">More</a>
</section>

<section class="solutions" role="img" aria-label="Dark photograph of a conference room with chairs">
  <h2>Commercial and Residential<br>Audio/Video and Automation System Solutions</h2>
</section>
</body>
</html>
```